Structural Engineering Business Card

Veltrow Drafts does residential house plans for clients in Central Florida. Would like simple but elegant business card that is appropriate for a house plan engineering company. Prefer black business card with black/white them but open to other shades of blue. I uploaded a sample card that I came across that looked good but please come up with your own creative designs.

Contact Information for Business Card

Name, Title, Phone, Email, Address, website

```html
<!DOCTYPE html>
<html lang="en">
<head>
<meta charset="UTF-8">
<title>Veltrow Drafts — Business Card</title>
<link href="https://fonts.googleapis.com/css2?family=Poppins:wght@400;700;800&display=swap" rel="stylesheet">
<style>
  :root {
    --bg: #e4e4e6;
    --navy: #05061d;
    --gold: #c99a2e;
    --white: #ffffff;
    --ink: #0b0b0b;
    --rule: #9a9a9a;
  }
  * { margin: 0; padding: 0; box-sizing: border-box; }
  html, body {
    width: 1200px; height: 1200px; overflow: hidden;
    background: var(--bg);
    font-family: 'Poppins', sans-serif;
  }
  .stage {
    position: relative; width: 1200px; height: 1200px;
  }
  .card {
    position: absolute; top: 303px;
    width: 368px; height: 594px;
  }
  .card--front { left: 201px; background: var(--navy); }
  .card--back { left: 600px; background: var(--white); color: var(--ink); }

  .wordmark {
    position: absolute; left: 0; right: 0;
    text-align: center; font-weight: 800;
    letter-spacing: 0.5px; text-transform: uppercase;
    white-space: nowrap;
  }
  .card--front .wordmark {
    top: 278px; font-size: 30px; color: var(--gold);
  }
  .card--back .wordmark {
    top: 168px; font-size: 32px; color: var(--ink);
  }

  .details {
    position: absolute; left: 0; right: 0; top: 336px;
    text-align: center;
  }
  .person-name { font-weight: 700; font-size: 21px; line-height: 26px; letter-spacing: 0.3px; }
  .person-title { font-weight: 400; font-size: 16px; line-height: 20px; }

  .icon-row {
    display: flex; align-items: center; justify-content: center;
    gap: 4px; margin-top: 13px;
  }
  .icon-row .rule { width: 52px; height: 1px; background: var(--rule); margin: 0 2px; }
  .icon {
    width: 25px; height: 25px; background: var(--ink); border-radius: 3px;
    display: flex; align-items: center; justify-content: center;
  }
  .icon svg { width: 15px; height: 15px; }

  .contact { margin-top: 8px; font-size: 16.5px; line-height: 21px; }
  .divider { width: 195px; height: 1px; background: var(--rule); margin: 17px auto 13px; }
  .address { font-size: 16.5px; line-height: 21px; }
</style>
</head>
<body>
<div class="stage">
  <section class="card card--front">
    <div class="wordmark">Veltrow Drafts</div>
  </section>

  <section class="card card--back">
    <div class="wordmark">Veltrow Drafts</div>
    <div class="details">
      <div class="person-name">MARCUS ELDEN</div>
      <div class="person-title">Managing Director</div>
      <div class="icon-row">
        <span class="rule"></span>
        <span class="icon" aria-label="Phone">
          <svg viewBox="0 0 24 24" fill="#fff"><path d="M3 9c0-2 4-4 9-4s9 2 9 4v2h-4V9c-1-.8-3-1.2-5-1.2S8 8.2 7 9v2H3z"/><path d="M7 12h10l2 7H5z"/></svg>
        </span>
        <span class="icon" aria-label="Email">
          <svg viewBox="0 0 24 24" fill="none" stroke="#fff" stroke-width="1.8"><rect x="3" y="6" width="18" height="12"/><path d="M3 6l9 7 9-7M3 18l7-6M21 18l-7-6"/></svg>
        </span>
        <span class="icon" aria-label="Website">
          <svg viewBox="0 0 24 24" fill="none" stroke="#fff" stroke-width="1.8"><circle cx="12" cy="12" r="9"/><path d="M3 12h18M12 3c3 3 3 15 0 18M12 3c-3 3-3 15 0 18"/></svg>
        </span>
        <span class="rule"></span>
      </div>
      <div class="contact">
        <div>044-555 018 273</div>
        <div>info@veltrowdrafts.com</div>
        <div>www.veltrowdrafts.com</div>
      </div>
      <div class="divider"></div>
      <div class="address">
        <div>421, Address line goes here</div>
        <div>45452,Country Name</div>
      </div>
    </div>
  </section>
</div>
</body>
</html>
```